LEAP GLIDE SOAR

Need a 4 X 6 post card design. Here are the elements that need to be on the card:
LEAP, GLIDE, SOAR (This is the title please feel free and create)
DATE: August 28, 2022
Showtimes 2:30 PM & 7:30 PM
Location: Harriet Colvane Theatre Fernhollow Creek, CA
Tickets can be purchased at:
http://colvanestagehall.tixora-example.com/LEAPGLIDESOAR or
by calling the ticket office at (555) 555-STAGE
LEAP, GLIDE, SOAR showcases the dance stylings of urban hip hop, ballet, modern jazz and much much more! Bay Area renown dancer/choreographer Rosa Janelle Pruitt headlines this cast of dancers and will amaze you as she takes you on a journey through dance that you will never forget. Join us for an experience that will prove to excite and delight you!
Now for the artwork I would like to incorporate all three of these photos. The photo entitled "beach" you are only to use the dancer on the left. So clip out the other dancer in the pink dress. The Garden photo and the beach photo the images need to be cut out from the background. The sidewalk photo you can leave the background (just my preference) but for the sake of the overall design I'm ok with removing its background as well.
Ok have at it. I want to end this competition in a few days so let's get these designs in. Thank you!

```html
<!DOCTYPE html>
<html lang="en">
<head>
<meta charset="utf-8">
<title>Leap Glide Soar — Postcard</title>
<link rel="stylesheet" href="https://fonts.googleapis.com/css2?family=Lobster&family=Montserrat+Alternates:wght@400;600;700&family=Oswald:wght@400&display=swap">
<style>
  :root {
    --violet-deep: #4f47c9;
    --violet: #7b5ce0;
    --violet-soft: #9a86e6;
    --sky: #9fd3ea;
    --peach: #f3d6c6;
    --magenta: #e02ca8;
    --magenta-dark: #b3137f;
    --pink-light: #fde0f1;
    --white: #ffffff;
    --ink-purple: #4a3fc4;
  }
  * { margin: 0; padding: 0; box-sizing: border-box; }
  html, body { width: 1200px; height: 800px; overflow: hidden; background: #d4d4d4; }

  .postcard {
    position: relative;
    width: 1200px;
    height: 800px;
    overflow: hidden;
    font-family: "Montserrat Alternates", sans-serif;
    color: var(--white);
    background:
      radial-gradient(ellipse 420px 260px at 560px 40px, var(--peach) 0%, rgba(243,214,198,0) 100%),
      radial-gradient(ellipse 380px 300px at 260px 20px, var(--sky) 0%, rgba(159,211,234,0) 100%),
      radial-gradient(ellipse 400px 420px at 1150px 520px, var(--peach) 0%, rgba(243,214,198,0) 100%),
      linear-gradient(160deg, var(--violet-soft) 0%, var(--violet) 45%, var(--violet-deep) 100%);
  }

  .backdrop { position: absolute; inset: 0; }

  .dancer-photo {
    position: absolute;
    left: 540px;
    top: 190px;
    width: 650px;
    height: 610px;
    background:
      radial-gradient(ellipse 110px 260px at 555px 370px, rgba(224,44,168,0.9) 0%, rgba(224,44,168,0) 100%),
      radial-gradient(ellipse 110px 270px at 430px 360px, rgba(250,248,255,0.85) 0%, rgba(250,248,255,0) 100%),
      radial-gradient(ellipse 150px 270px at 280px 390px, rgba(30,24,40,0.85) 0%, rgba(30,24,40,0) 100%),
      radial-gradient(ellipse 260px 80px at 320px 100px, rgba(140,90,200,0.7) 0%, rgba(140,90,200,0) 100%);
  }

  .title {
    position: absolute;
    left: 218px;
    top: 30px;
    font-family: "Lobster", cursive;
    font-size: 108px;
    line-height: 1;
    color: var(--pink-light);
    transform: rotate(-3deg);
    transform-origin: left bottom;
    white-space: nowrap;
    text-shadow:
      1px 1px 0 var(--magenta),
      2px 2px 0 var(--magenta),
      3px 3px 0 var(--magenta),
      4px 4px 0 var(--magenta-dark),
      5px 5px 0 var(--magenta-dark),
      6px 8px 10px rgba(80,20,90,0.35);
  }

  .tagline {
    position: absolute;
    left: 234px;
    top: 146px;
    width: 730px;
    height: 52px;
    background: var(--magenta);
    transform: rotate(-3deg);
    display: flex;
    align-items: center;
    justify-content: center;
    font-weight: 700;
    font-size: 20px;
    white-space: nowrap;
  }

  .description {
    position: absolute;
    left: 66px;
    top: 232px;
    width: 466px;
    text-align: center;
    font-size: 19px;
    line-height: 25px;
  }
  .description strong { font-weight: 700; }

  .tickets-cta {
    position: absolute;
    left: 100px;
    top: 420px;
    width: 366px;
    height: 50px;
    background: var(--magenta);
    transform: rotate(-2deg);
    display: flex;
    align-items: center;
    justify-content: center;
    font-weight: 600;
    font-size: 25px;
  }

  .tickets-url {
    position: absolute;
    left: 108px;
    top: 468px;
    width: 350px;
    height: 70px;
    background: var(--white);
    transform: rotate(-2deg);
    color: var(--ink-purple);
    display: flex;
    align-items: center;
    justify-content: center;
    text-align: center;
    font-size: 16px;
    line-height: 20px;
  }

  .day {
    position: absolute;
    left: 76px;
    top: 574px;
    font-family: "Oswald", sans-serif;
    font-size: 104px;
    line-height: 1;
    letter-spacing: -4px;
    transform: scaleX(0.78);
    transform-origin: left top;
  }
  .day-suffix {
    position: absolute;
    left: 146px;
    top: 566px;
    font-family: "Oswald", sans-serif;
    font-size: 34px;
    line-height: 1;
    transform: scaleX(0.78);
    transform-origin: left top;
  }
  .month {
    position: absolute;
    left: 176px;
    top: 568px;
    background: var(--white);
    color: var(--ink-purple);
    font-weight: 700;
    font-size: 24px;
    line-height: 34px;
    padding: 0 12px;
    white-space: nowrap;
  }
  .showtimes {
    position: absolute;
    left: 174px;
    top: 610px;
    font-weight: 600;
    font-size: 30px;
    line-height: 31px;
    white-space: nowrap;
  }

  .divider {
    position: absolute;
    left: 326px;
    top: 564px;
    width: 2px;
    height: 116px;
    background: var(--magenta);
  }

  .contact { position: absolute; left: 352px; top: 566px; font-size: 20px; line-height: 24px; }
  .contact-row { display: flex; align-items: flex-start; gap: 16px; margin-bottom: 12px; }
  .contact-row svg { flex: none; margin-top: 1px; }
</style>
</head>
<body>
  <main class="postcard">
    <svg class="backdrop" width="1200" height="800" viewBox="0 0 1200 800" aria-hidden="true">
      <defs>
        <radialGradient id="haloFill" cx="0.5" cy="0.5" r="0.5">
          <stop offset="0" stop-color="#c9b4e8" stop-opacity="0.9"/>
          <stop offset="0.7" stop-color="#7a60dc" stop-opacity="0.6"/>
          <stop offset="1" stop-color="#5a48d2" stop-opacity="0"/>
        </radialGradient>
      </defs>
      <circle class="stage-halo" cx="890" cy="470" r="360" fill="url(#haloFill)"/>
      <circle class="stage-ring" cx="890" cy="470" r="300" fill="none" stroke="#ffffff" stroke-opacity="0.55" stroke-width="3"/>
      <circle class="stage-ring" cx="890" cy="470" r="255" fill="none" stroke="#ffffff" stroke-opacity="0.3" stroke-width="2"/>
    </svg>

    <div class="dancer-photo" role="img" aria-label="Photo cut-out of three dancers: one leaping in black with a violet scarf, one in white, and the headliner in a magenta dress"></div>

    <h1 class="title">Leap Glide Soar</h1>
    <p class="tagline">Join us for an experience that will prove to excite &amp; delight you!</p>

    <p class="description">
      <strong>LEAP, GLIDE, SOAR</strong> showcases the dance stylings of urban hip hop, ballet, modern jazz &amp; much much more! Bay Area renown dancer/choreographer <strong>Rosa Janelle Pruitt</strong> headlines this cast of dancers &amp; will amaze you as she takes you on a journey through dance that you will never forget.
    </p>

    <p class="tickets-cta">Book your tickets NOW!</p>
    <p class="tickets-url">colvanestagehall.tixora-example.com<br>/LEAPGLIDESOAR</p>

    <span class="day">28</span>
    <span class="day-suffix">th</span>
    <span class="month">August</span>
    <p class="showtimes">2:30 pm<br>7:30 pm</p>

    <div class="divider"></div>

    <div class="contact">
      <p class="contact-row">
        <svg width="20" height="20" viewBox="0 0 24 24" aria-hidden="true"><path fill="#fff" d="M6.6 10.8a15.1 15.1 0 0 0 6.6 6.6l2.2-2.2a1 1 0 0 1 1-.25 11.4 11.4 0 0 0 3.6.57 1 1 0 0 1 1 1V20a1 1 0 0 1-1 1A17 17 0 0 1 3 4a1 1 0 0 1 1-1h3.5a1 1 0 0 1 1 1c0 1.25.2 2.45.57 3.57a1 1 0 0 1-.25 1z"/></svg>
        <span>(555) 555-STAGE</span>
      </p>
      <p class="contact-row">
        <svg width="20" height="22" viewBox="0 0 24 26" aria-hidden="true"><path fill="#fff" d="M12 1a8 8 0 0 0-8 8c0 6 8 15 8 15s8-9 8-15a8 8 0 0 0-8-8zm0 11a3 3 0 1 1 0-6 3 3 0 0 1 0 6z"/></svg>
        <span>Harriet Colvane<br>Theatre Fernhollow<br>Creek, CA</span>
      </p>
    </div>
  </main>
</body>
</html>
```